Skill Up Salary Up

Full Page
7.5 w x 10 h / 8 w x 10.75 h + .25" bleed
Full-Page Career Course Ad
Project Overview
• Goal: Create a visually attractive, modern, and uncluttered full-page magazine advertisement to list available career courses.
• Tone: Creative, professional, and attention-grabbing to prevent the reader from turning the page. The final design must prioritize readability.

Content Requirements
1. Header/Headline: Must be the primary focus. And grab peoples attention
2. Course Listing: A clear, well-organized list of the career courses.
________________________________________
Design & Aesthetic Directives
1. Layout & Readability (Crucial)
• The final ad must not look crowded or busy.
• Prioritize white space to make the text "breathe" and ensure the course list is easy to scan and read.
• Use a modern, clean, and professional typeface (font choice is critical for the aesthetic).
2. Visual Style
• Aim for a creative, modern, and fresh look. Avoid outdated or generic stock imagery/layouts.
3. Imagery/Graphic Element (Artist's Choice)
You have creative freedom regarding the main graphic element.
• Option A (Photography): Use a photo of a white male American with a collared shirt. The imagery should convey success, focus, or professional development.
• Option B (Vector/Illustration): Use a modern vector graphic, illustration, or abstract design. This could be used to symbolize growth, connection, or a career path.
The choice of graphic element is yours, but it must support the overall modern and uncrowded aesthetic.

Requirements
Must have
• Partial listing .. is part of the Harbor Lantern Course

```html
<!DOCTYPE html>
<html lang="en">
<head>
<meta charset="utf-8">
<title>Skill Up, Salary Up — Upcoming HLC Courses</title>
<link href="https://fonts.googleapis.com/css2?family=Bebas+Neue&family=Poppins:wght@400;500;600;700;800&display=swap" rel="stylesheet">
<style>
:root{
  --stage:#b0b0b0;
  --bleed:#f2f3f5;
  --page:#ffffff;
  --card:#f2f3f5;
  --footer:#d6d7d9;
  --orange:#f58634;
  --navy:#1a4a8a;
  --blue:#1f62a3;
  --ink:#111111;
  --photo-a:#e9ecef;
  --photo-b:#c9d6e6;
}
*{margin:0;padding:0;box-sizing:border-box}
html,body{width:908px;height:1200px;overflow:hidden}
body{background:var(--stage);position:relative;font-family:"Poppins",sans-serif;color:var(--ink)}
.bleed-area{position:absolute;left:82px;top:82px;width:744px;height:1036px;background:var(--bleed)}
.trim-page{position:absolute;left:103px;top:104px;width:702px;height:908px;background:var(--page)}
.footer-bleed{position:absolute;left:103px;top:1012px;width:702px;height:84px;background:var(--footer);
  display:flex;align-items:center;justify-content:center;color:#f6f6f6;font-weight:700;font-size:27px;letter-spacing:5px}

.headline-top{position:absolute;left:139px;top:131px;color:var(--orange);font-weight:800;font-size:51px;line-height:44px;letter-spacing:-0.5px}
.headline-main{position:absolute;left:139px;top:232px;color:var(--navy);font-family:"Bebas Neue",sans-serif;font-size:88px;line-height:67px;letter-spacing:-0.5px}
.tag{position:absolute;height:24px;border-radius:5px;color:#fff;font-weight:500;font-size:13.5px;line-height:24px;padding:0 7px;white-space:nowrap}
.tag--navy{background:var(--navy)}
.tag--blue{background:var(--blue)}

.hero-photo{position:absolute;left:494px;top:133px;width:274px;height:290px}

.course-card{position:absolute;background:var(--card);padding-left:32.5px}
.course-title{color:var(--orange);font-weight:600;font-size:16px;line-height:20px;white-space:nowrap}
.course-lead{font-weight:600;font-size:12.5px;line-height:15px}
.course-lead--large{font-size:16px;line-height:20px}
.course-label{color:var(--orange);font-weight:600;font-size:12.5px;line-height:15px}
.course-duration{color:var(--navy);font-weight:700;font-size:16px;line-height:15px}
.check-list{list-style:none}
.check-list li{position:relative;padding-left:11px;font-size:11.3px;line-height:17.2px;white-space:nowrap}
.check-list li::before{content:"";position:absolute;left:0;top:5.2px;width:7px;height:7px;border-radius:50%;background:var(--orange)}
.check-list li::after{content:"";position:absolute;left:2.3px;top:6.6px;width:2.2px;height:3.4px;border:solid #fff;border-width:0 1.2px 1.2px 0;transform:rotate(45deg)}
.check-list--two{display:grid;grid-template-columns:var(--col,126px) auto}
</style>
</head>
<body>
<div class="bleed-area"></div>
<div class="trim-page"></div>

<div class="headline-top">SKILL UP,<br>SALARY UP</div>
<div class="headline-main">UPCOMING<br>HLC COURSES</div>

<div class="tag tag--navy" style="left:139.5px;top:381.5px">MEN &amp; WOMEN</div>
<div class="tag tag--blue" style="left:258px;top:381.5px">IN-PERSON &amp; REMOTE</div>
<div class="tag tag--navy" style="left:139.5px;top:410px">PARTIAL SCHOLORASHIPS</div>

<svg class="hero-photo" viewBox="0 0 274 290">
  <defs>
    <linearGradient id="photoTone" x1="0" y1="0" x2="1" y2="1">
      <stop offset="0" stop-color="var(--photo-a)"/>
      <stop offset="1" stop-color="var(--photo-b)"/>
    </linearGradient>
  </defs>
  <circle cx="137" cy="150" r="131" fill="none" stroke="var(--orange)" stroke-width="13"/>
  <circle cx="137" cy="150" r="125" fill="url(#photoTone)" role="img" aria-label="Photo of a smiling young male student in a blue checked collared shirt with a backpack, holding a laptop"/>
</svg>

<section class="course-card" style="left:139.5px;top:453px;width:302.5px;height:312px;padding-top:11px">
  <h2 class="course-title">Harbor Lantern</h2>
  <p class="course-lead course-lead--large" style="margin-top:1px">Business Skills &amp; Knowledge to:</p>
  <ul class="check-list">
    <li>Impress your interviewer</li>
    <li>Maximize Income</li>
    <li>Start / Run Your Business</li>
  </ul>
  <p class="course-duration" style="margin-top:6.5px">4-5 MONTHS<br>NOV&nbsp; 2025</p>
  <h3 class="course-title" style="margin-top:21.5px">PARTIAL LISTING</h3>
  <ul class="check-list check-list--two" style="margin-top:0.4px">
    <li>Computers</li><li>Communication</li>
    <li>Marketing</li><li>LedgerBooks</li>
    <li>Sales</li><li>Investments</li>
    <li>Finance</li><li>Real Estate</li>
    <li>Healthcare</li><li>Accounting</li>
    <li>Business Strategy</li>
  </ul>
</section>

<section class="course-card" style="left:456px;top:453px;width:312px;height:170px;padding-top:11px">
  <h2 class="course-title">Bookkeeping LedgerBooks</h2>
  <p class="course-lead" style="margin-top:5.5px">Train for a quality job<br>Manage your own books</p>
  <ul class="check-list" style="margin-top:5px">
    <li>Finance Management</li>
    <li>Customer &amp; Vendor Mgmt.</li>
    <li>Advanced Tools</li>
  </ul>
  <p class="course-duration" style="margin-top:5.5px">5 WEEKS<br>NOV&nbsp; 2025</p>
</section>

<section class="course-card" style="left:456px;top:635.5px;width:312px;height:170px;padding-top:8px">
  <h2 class="course-title">IT Desktop &amp; Networking Support</h2>
  <p class="course-lead" style="margin-top:4.5px">#2 Best Job<br>National Career Review 2025</p>
  <p class="course-label" style="margin-top:5px">Masters IT:</p>
  <ul class="check-list check-list--two" style="--col:78px;margin-top:2px">
    <li>Desktop OS</li><li>Servers</li>
    <li>Networks</li><li>Cloud</li>
  </ul>
  <p class="course-duration" style="margin-top:8.7px">7 MONTHS<br>Dec 2025</p>
</section>

<section class="course-card" style="left:139.5px;top:776px;width:302.5px;height:209px;padding-top:16.6px">
  <h2 class="course-title">Software, Web &amp; Apps</h2>
  <p class="course-lead" style="margin-top:1px"># 2 Best Tech Job<br>National Career Review 2025</p>
  <p class="course-label" style="margin-top:9px">Job Opportunities</p>
  <ul class="check-list" style="margin-top:1px">
    <li>Computer Programmer</li>
    <li>Software Developer/Mobile</li>
    <li>Engineer Developer (Apps</li>
  </ul>
  <p class="course-lead" style="margin-top:7.5px">Optional: Bachelors in Prog. &amp; Tech.</p>
  <p class="course-duration" style="margin-top:6px">NOV&nbsp; 2025</p>
</section>

<section class="course-card" style="left:456px;top:818px;width:312px;height:167px;padding-top:8.3px">
  <h2 class="course-title">Office Suite- Computers</h2>
  <p class="course-lead" style="margin-top:7.2px">The New&nbsp;&nbsp; Job Prerequisite</p>
  <ul class="check-list check-list--two" style="--col:78px;margin-top:4.9px">
    <li>Sheets</li><li>Email</li>
    <li>Docs</li><li>Slides</li>
  </ul>
  <p class="course-label" style="margin-top:3.7px">Computer lab available to practice</p>
  <p class="course-duration" style="margin-top:7.5px">5 WEEKS<br>DEC 2025</p>
</section>

<div class="footer-bleed">FOOTER BLEED 1 INCH</div>
</body>
</html>
```